General Dental Office Business Card

I run a private general dental office in southern California, and would like a refresh/redesign of my business card. I focus on quality care rather than volume. The email address on the uploaded current card should be updated to: info@marbleshoredental.example. The current card's logo is a deboss, but I am open to other ideas. The logo can be refreshed, but it is something that's been with me since the beginning of the office, so I wouldn't want a drastic redesign.
Target Market(s)
Adults 18-99, whoever needs dental services
Industry/Entity Type
Healthcare/Dental
Contact Information for Business Card
Name, Address, Phone, email
Colors
Designer to choose colors to be used in the design.
Requirements
Must have
- Logo (Same as original one in the uploaded file), space on back for appointment time/date

```html
<!DOCTYPE html>
<html lang="en">
<head>
<meta charset="utf-8">
<title>Marble Shore Dental – Business Card</title>
<link rel="stylesheet" href="https://fonts.googleapis.com/css2?family=Montserrat:wght@600&family=Source+Sans+3:wght@400;600&display=swap">
<style>
  :root {
    --teal: #4fb8d0;
    --teal-faint: #e9f5f9;
    --ink: #595a5c;
    --card: #ffffff;
    --backdrop: #3b3c3d;
  }
  * { box-sizing: border-box; margin: 0; padding: 0; }
  html, body { width: 1200px; height: 1059px; overflow: hidden; background: var(--backdrop); }
  body { position: relative; font-family: "Source Sans 3", sans-serif; color: var(--ink); }

  .card {
    position: absolute;
    left: 256px;
    width: 688px;
    height: 392px;
    background: var(--card);
    border-radius: 20px;
  }
  .card--front { top: 100px; }
  .card--back { top: 537px; }

  /* front */
  .mark {
    position: absolute;
    left: 110px; top: 99px;
    width: 158px; height: 158px;
    border: 6px solid var(--teal);
    border-radius: 50%;
    display: flex; align-items: center; justify-content: center;
    text-align: center;
    font-family: "Montserrat", sans-serif; font-weight: 600;
    font-size: 15px; line-height: 1.25; color: var(--teal);
  }
  .divider {
    position: absolute;
    left: 301px; top: 100px;
    width: 1.5px; height: 187px;
    background: var(--teal);
  }
  .details { position: absolute; left: 328px; top: 95px; }
  .details__name {
    font-weight: 600; font-size: 29px; line-height: 32px; color: var(--teal);
  }
  .details__role { font-size: 16.5px; line-height: 19px; margin-top: -1px; }
  .details__address { font-size: 16.5px; line-height: 23px; margin-top: 16px; }
  .details__contact { list-style: none; margin-top: 14px; }
  .details__contact li {
    display: flex; align-items: center; gap: 8px;
    font-size: 17px; line-height: 23px;
  }
  .details__contact svg { width: 13px; height: 13px; fill: var(--teal); flex: none; }
  .brand-line {
    position: absolute; left: 0; right: 0; top: 330px;
    text-align: center;
    font-family: "Montserrat", sans-serif; font-weight: 600;
    font-size: 33px; letter-spacing: 3px; color: var(--teal);
  }

  /* back */
  .back-title {
    position: absolute; left: 0; right: 0; top: -26px;
    text-align: center; white-space: nowrap;
    font-family: "Montserrat", sans-serif; font-weight: 600;
    font-size: 56px; letter-spacing: 2px; line-height: 70px; color: var(--teal);
  }
  .mark--faint {
    left: 247px; top: 74px; width: 200px; height: 200px;
    border: 8px solid var(--teal-faint);
    color: var(--teal-faint); font-size: 19px;
  }
  .appointment {
    position: absolute; left: 42px; top: 345px;
    display: flex; align-items: baseline;
    font-size: 18px; white-space: nowrap;
  }
  .appointment__blank {
    display: inline-block; width: 196px; height: 1px;
    border-bottom: 1.5px dashed var(--ink); margin-right: 3px;
  }
</style>
</head>
<body>

<section class="card card--front" aria-label="Card front">
  <div class="mark">Marble<br>Shore<br>Dental</div>
  <div class="divider"></div>
  <div class="details">
    <h1 class="details__name">Daniel R. Moss DDS</h1>
    <p class="details__role">General Dentistry</p>
    <p class="details__address">1820 Seacrest Avenue<br>Lakeview, CA 92000</p>
    <ul class="details__contact">
      <li>
        <svg viewBox="0 0 16 16" aria-hidden="true"><path d="M1 6c0-2 3-3 7-3s7 1 7 3v1h-4V5.5H5V7H1z"/><rect x="3" y="8" width="10" height="6" rx="1"/></svg>
        555-014-2828
      </li>
      <li>
        <svg viewBox="0 0 16 16" aria-hidden="true"><path d="M1 3h14v10H1z M2.5 4.5 8 9l5.5-4.5" fill="none" stroke="#4fb8d0" stroke-width="2"/></svg>
        info@marbleshoredental.example
      </li>
      <li>
        <svg viewBox="0 0 16 16" aria-hidden="true"><circle cx="8" cy="8" r="6.5" fill="none" stroke="#4fb8d0" stroke-width="1.5"/><path d="M4 5c2 0 2 2 4 2s1 3-1 4M10 3c0 2 2 2 3 3"/></svg>
        www.marbleshoredental.example
      </li>
    </ul>
  </div>
  <p class="brand-line">Marble Shore Dental</p>
</section>

<section class="card card--back" aria-label="Card back">
  <p class="back-title">Marble Shore Dental</p>
  <div class="mark mark--faint">Marble<br>Shore<br>Dental</div>
  <p class="appointment">
    Appointment Date:<span class="appointment__blank"></span>Time:<span class="appointment__blank"></span>
  </p>
</section>

</body>
</html>
```